Junior Kickstart Academy needs modern,elegant Letterhead

Our school needs a modern Letterhead with header a footer for Electronic and Hardcopy. Busuness Cards, Envelopes and Powerpoint template.
The header/footer are to have:
The school name: Torvald Miskey School of Football
School moto - "I think, therefore I am"

Contact details: Address: 14 Lindale Street, Brookmere, Harare, Zimbabwe

Mobiles: +263 77 418 3672, +263 77 539 8106
website (some of these things could be in the footer)
Email: dmiskey@tmsk-example.org
School website is www.tmsk-example.org

Registar of Deeds# KT417/2011

Industry/Entity Type

School

Font styles to use
Serif

```html
<!DOCTYPE html>
<html lang="en">
<head>
<meta charset="utf-8">
<title>Junior Kickstart Academy – Stationery</title>
<link href="https://fonts.googleapis.com/css2?family=Tinos:wght@400;700&family=Play:wght@400&display=swap" rel="stylesheet">
<style>
  :root{
    --stage:#676767;
    --paper:#ffffff;
    --ink:#222222;
    --muted:#444444;
    --green:#1fa64a;
    --yellow:#f3bd1b;
    --red:#8e1a1c;
    --accent-red:#c4161c;
    --serif:"Tinos","Times New Roman",serif;
    --display:"Play","Trebuchet MS",sans-serif;
  }
  *{box-sizing:border-box;margin:0;padding:0}
  html,body{width:1200px;height:1000px;overflow:hidden}
  body{background:var(--stage);position:relative;font-family:var(--serif);color:var(--ink)}
  .sheet{position:absolute;background:var(--paper);box-shadow:0 2px 6px rgba(0,0,0,.35)}

  .brand{display:flex;align-items:center;gap:8px;font-family:var(--serif);color:var(--ink);font-weight:700;white-space:nowrap}
  .brand-dot{width:14px;height:14px;border-radius:50%;background:var(--green);flex:none}
  .motto{font-family:var(--serif);letter-spacing:.3px;color:var(--ink);white-space:nowrap}
  .contacts{list-style:none;font-size:11px;color:var(--muted)}
  .contacts li{display:flex;align-items:center;gap:5px;height:16px;white-space:nowrap}
  .icon{width:9px;height:9px;border-radius:2px;background:var(--accent-red);position:relative;flex:none}
  .icon::after{content:"";position:absolute;left:2px;top:2px;width:5px;height:5px;background:#fff;border-radius:1px}
  .corner-art{position:absolute;background:linear-gradient(160deg,var(--green) 0%,var(--yellow) 55%,var(--red) 100%);opacity:.9}
  .tri-rule{position:absolute;display:flex;height:4px}
  .tri-rule span{height:100%}
  .g{background:var(--green)} .y{background:var(--yellow)} .r{background:var(--red)}

  /* Letterhead */
  .letterhead{left:33px;top:43px;width:667px;height:862px}
  .letterhead .brand{position:absolute;left:44px;top:62px;font-size:13px}
  .letterhead .motto{position:absolute;left:42px;top:100px;font-size:12.5px}
  .letterhead .contacts{position:absolute;left:520px;top:20px}
  .letterhead .corner-art{left:25px;top:790px;width:60px;height:72px}
  .footer-address{position:absolute;left:105px;top:816px;font-size:12px;color:var(--muted);white-space:nowrap}
  .footer-reg{position:absolute;left:105px;top:833px;font-size:9.5px;color:var(--muted);white-space:nowrap}
  .letterhead .tri-rule{left:257px;top:837px;width:410px}

  /* Envelope */
  .envelope{left:420px;top:150px;width:730px;height:300px;overflow:hidden}
  .envelope .brand{position:absolute;left:36px;top:50px;font-size:12px}
  .envelope .contacts{position:absolute;left:62px;top:110px;font-size:10px}
  .envelope .contacts li{height:14px}
  .envelope .address{position:absolute;left:77px;top:168px;font-size:10px;line-height:1.25;color:var(--accent-red)}
  .envelope .tri-rule{left:0;bottom:0;width:100%;height:18px}

  /* Business cards */
  .card{width:410px;height:240px}
  .card-front{left:760px;top:475px;overflow:hidden}
  .card-front .corner-art{left:0;top:0;width:150px;height:240px}
  .person-name{position:absolute;left:218px;top:28px;font-family:var(--display);font-weight:400;font-size:19px;color:var(--red);white-space:nowrap}
  .person-role{position:absolute;left:219px;top:53px;font-size:11px;color:var(--muted)}
  .card-front .contacts{position:absolute;left:218px;top:121px;font-size:11px}
  .card-front .address{position:absolute;left:218px;top:185px;font-size:11px;line-height:1.2;color:var(--muted)}
  .card-back{left:760px;top:735px}
  .card-back .brand{position:absolute;left:0;right:0;top:72px;justify-content:center;font-size:19px}
  .card-back .motto{position:absolute;left:0;right:0;top:184px;text-align:center;font-size:14px}
</style>
</head>
<body>

<section class="sheet letterhead" aria-label="Letterhead">
  <div class="brand"><span class="brand-dot"></span><span>Torvald Miskey School of Football</span></div>
  <p class="motto">I THINK, THEREFORE I AM</p>
  <ul class="contacts">
    <li><span class="icon"></span>+263 77 418 3672</li>
    <li><span class="icon"></span>+263 77 539 8106</li>
    <li><span class="icon"></span>dmiskey@tmsk-example.org</li>
    <li><span class="icon"></span>www.tmsk-example.org</li>
  </ul>
  <div class="corner-art" role="img" aria-label="Decorative corner artwork in green, yellow and red"></div>
  <p class="footer-address">14 Lindale Street, Brookmere Harare, Zimbabwe</p>
  <p class="footer-reg">Registar of Deeds# KT417/2011</p>
  <div class="tri-rule"><span class="g" style="width:63%"></span><span class="y" style="width:19%"></span><span class="r" style="width:18%"></span></div>
</section>

<section class="sheet envelope" aria-label="Envelope">
  <div class="brand"><span class="brand-dot"></span><span>Torvald Miskey School of Football</span></div>
  <ul class="contacts">
    <li><span class="icon"></span>+263 77 418 3672</li>
    <li><span class="icon"></span>+263 77 539 8106</li>
    <li><span class="icon"></span>dmiskey@tmsk-example.org</li>
    <li><span class="icon"></span>www.tmsk-example.org</li>
  </ul>
  <p class="address">14 Lindale Street, Brookmere<br>Harare, Zimbabwe</p>
  <div class="tri-rule"><span class="g" style="width:73%"></span><span class="y" style="width:10%"></span><span class="r" style="width:17%"></span></div>
</section>

<section class="sheet card card-front" aria-label="Business card front">
  <div class="corner-art" role="img" aria-label="Decorative side artwork in green, yellow and red"></div>
  <h1 class="person-name">Daniel Orwen</h1>
  <p class="person-role">Director</p>
  <ul class="contacts">
    <li><span class="icon"></span>+263 77 418 3672</li>
    <li><span class="icon"></span>+263 77 539 8106</li>
    <li><span class="icon"></span>dmiskey@tmsk-example.org</li>
    <li><span class="icon"></span>www.tmsk-example.org</li>
  </ul>
  <p class="address">14 Lindale Street, Brookmere<br>Harare, Zimbabwe</p>
</section>

<section class="sheet card card-back" aria-label="Business card back">
  <div class="brand"><span class="brand-dot"></span><span>Torvald Miskey School of Football</span></div>
  <p class="motto">I THINK, THEREFORE I AM</p>
</section>

</body>
</html>
```